Velder Crest is a new and completely innovative health supplement aimed at males between the ages of 25-60.

The supplement is formulated specifically to address two significant factors that affect men as they age. A reduction in the primary sex hormones and a reduction in their fertility.

I already have the logo design and label designed. I am looking to launch the product in January/February following successful trials.
The website won't need to have selling features inbuilt as I will be going through 3rd party platforms.

The website will however need to direct traffic to websites for a couple of purposes. In total I would expect to have in the region of 5-6 pages in total.

```html
<!DOCTYPE html>
<html lang="en">
<head>
<meta charset="utf-8">
<title>Velder Crest</title>
<link href="https://fonts.googleapis.com/css2?family=Archivo+Black&family=Poppins:wght@400;500;600;700&display=swap" rel="stylesheet">
<style>
:root{--blue:#00aeef;--blue-dark:#0a8fd0;--black:#0b0b0b;--white:#fff;--grey:#555;--light:#eef3f6}
*{margin:0;padding:0;box-sizing:border-box}
html,body{width:1200px;height:4216px;overflow:hidden}
body{position:relative;font-family:'Poppins',sans-serif;color:var(--black);background:var(--white)}
.abs{position:absolute}
.brand{font-family:'Poppins',sans-serif;font-weight:700;font-size:26px;color:var(--black);display:flex;align-items:center;gap:10px}
.brand i{display:block;width:18px;height:18px;border-radius:50%;background:var(--blue)}
.topbar{left:0;top:0;width:1200px;height:64px}
.contact-top{top:18px;color:var(--white);font-size:19px;display:flex;align-items:center;gap:12px}
.nav{top:86px;left:248px;display:flex;font-size:20px;font-weight:500}
.nav span{margin-right:0}
.btn{display:flex;align-items:center;justify-content:center;color:var(--white);font-weight:500;text-transform:uppercase}
.btn.black{background:var(--black)}
.btn.blue{background:var(--blue)}
.hero-title{left:62px;top:278px;font-family:'Archivo Black',sans-serif;font-size:49px;line-height:63px;text-transform:uppercase}
.hero-title .w{color:var(--white)}
.small{font-size:11px;line-height:19px}
.bottle{background:linear-gradient(180deg,#f4f4f4,#dcdcdc);border-radius:30px}
.section-title{font-size:44px;font-weight:600;line-height:54px}
.section-title b{color:var(--blue);font-weight:600}
.center{text-align:center}
.benefit{width:300px;text-align:center;color:var(--white)}
.benefit h3{font-size:23px;font-weight:500;line-height:30px;margin-bottom:8px}
.benefit p{font-size:11px;line-height:18px}
.hex{width:104px;height:104px}
.why-item h4{font-size:23px;font-weight:600}
.why-item p{font-size:7px;line-height:12px;color:#333}
.tick{width:90px;height:90px}
.review{width:300px;text-align:center}
.review .stars{color:var(--blue);font-size:19px;letter-spacing:4px}
.review p{font-size:15px;line-height:22px;color:#444;margin-top:20px}
.person{display:flex;align-items:center;gap:16px;text-align:left}
.avatar{width:56px;height:56px;border-radius:50%;background:linear-gradient(135deg,#d9c2b0,#8c6f5c)}
.person b{display:block;font-size:16px;font-weight:500}
.person small{font-size:12px;color:#888}
.quote{font-family:'Archivo Black',sans-serif;font-size:64px;color:var(--blue);line-height:1}
.footer{left:0;top:3805px;width:1200px;height:353px;background:var(--black);color:var(--white)}
.footer h5{font-size:22px;font-weight:500}
.footer li{list-style:none;font-size:14px;display:flex;align-items:center;gap:12px;margin-bottom:21px}
.footer li::before{content:"";width:14px;height:16px;border:2px solid var(--blue);border-radius:3px}
.copy{left:0;top:4158px;width:1200px;height:58px;background:var(--blue);color:var(--white);font-size:20px}
.social{width:22px;height:22px;border-radius:50%;background:var(--black);top:18px}
</style>
</head>
<body>

<!-- Header -->
<svg class="abs topbar" viewBox="0 0 1200 64"><path d="M535 0H1200V64H640Z" fill="var(--blue)"/></svg>
<div class="abs brand" style="left:56px;top:38px"><i></i>Velder Crest</div>
<div class="abs contact-top" style="left:712px"><svg width="26" height="26"><circle cx="13" cy="13" r="13" fill="#111"/><rect x="9" y="6" width="8" height="14" rx="2" fill="#fff"/></svg>(123) 456 789</div>
<div class="abs contact-top" style="left:950px"><svg width="26" height="26"><circle cx="13" cy="13" r="13" fill="#111"/><rect x="7" y="8" width="12" height="10" fill="#fff"/><path d="M7 8l6 5 6-5" stroke="#111" fill="none"/></svg>info@website.com</div>
<nav class="abs nav">
  <span style="position:absolute;left:0">HOME</span>
  <span style="position:absolute;left:131px">ABOUT</span>
  <span style="position:absolute;left:260px">BENEFITS</span>
  <span style="position:absolute;left:391px;white-space:nowrap">TESTIMONIALS</span>
  <span style="position:absolute;left:589px">CONTACT</span>
</nav>
<div class="abs btn black" style="left:1011px;top:78px;width:160px;height:42px;font-size:20px;font-weight:400">Order Now</div>

<!-- Hero -->
<svg class="abs" style="left:0;top:130px" width="1200" height="830" role="img" aria-label="Couple in a bedroom holding a supplement bottle, tinted blue">
  <defs><linearGradient id="heroFill" x1="0" y1="0" x2="1" y2="1"><stop offset="0" stop-color="#17b4ef"/><stop offset="1" stop-color="#0aa3e3"/></linearGradient></defs>
  <path d="M4 0H1200V570C1150 720 1010 830 870 822C700 812 610 680 420 610C260 555 110 560 4 570Z" fill="url(#heroFill)"/>
</svg>
<div class="abs hero-title"><span class="w">Advanced</span><br>Multi-Complexed<br><span class="w">Formula for Men</span></div>
<p class="abs small" style="left:69px;top:483px;color:#fff;width:480px">Lorem ipsum dolor sit amet, consectetur adipiscing elit, sed do eiusmod tempor incididunt ut labore et dolore magna aliqua. Ut enim ad minim veniam.</p>
<div class="abs btn black" style="left:69px;top:552px;width:140px;height:32px;font-size:17px">Buy Now</div>
<div class="abs bottle" style="left:750px;top:328px;width:280px;height:430px" role="img" aria-label="Supplement bottle with red and yellow capsules"></div>

<!-- About -->
<div class="abs bottle" style="left:125px;top:965px;width:280px;height:438px" role="img" aria-label="Supplement bottle with red and yellow capsules"></div>
<h2 class="abs section-title" style="left:602px;top:1078px">VELDER <b>CREST</b></h2>
<div class="abs small" style="left:606px;top:1150px;width:510px">
  <p>Lorem ipsum dolor sit amet, consectetur adipiscing elit, sed do eiusmod tempor incididunt ut labore et dolore magna aliqua. Ut enim ad minim veniam, quis nostrud exercitation ullamco laboris nisi ut aliquip ex ea commodo consequat.</p>
  <p style="margin-top:10px">Lorem ipsum dolor sit amet, consectetur adipiscing elit, sed do eiusmod tempor incididunt ut labore et dolore magna aliqua. Ut enim ad minim veniam, quis nostrud exercitation ullamco laboris nisi ut aliquip ex ea commodo consequat.</p>
</div>
<div class="abs btn blue" style="left:606px;top:1296px;width:142px;height:40px;font-size:14px">Buy Now</div>

<!-- Benefits -->
<div class="abs" style="left:4px;top:1483px;width:1192px;height:495px;background:var(--blue)"></div>
<h2 class="abs section-title center" style="left:0;top:1528px;width:1192px;line-height:56px">BENEFITS OF<br><b style="color:#fff">VELDER CREST</b></h2>
<svg class="abs" style="left:0;top:1670px" width="1200" height="120">
  <line x1="200" y1="83" x2="445" y2="83" stroke="#000" stroke-width="5"/><circle cx="445" cy="83" r="10" fill="#000"/>
  <line x1="580" y1="88" x2="830" y2="88" stroke="#000" stroke-width="5"/><circle cx="830" cy="88" r="10" fill="#000"/>
  <g fill="#000"><polygon points="198,5 250,33 250,89 198,117 146,89 146,33"/><polygon points="578,5 630,33 630,89 578,117 526,89 526,33"/><polygon points="965,5 1017,33 1017,89 965,117 913,89 913,33"/></g>
  <circle cx="198" cy="61" r="30" fill="none" stroke="#fff" stroke-width="3"/>
  <rect x="568" y="44" width="20" height="34" rx="4" fill="none" stroke="#fff" stroke-width="3"/>
  <circle cx="955" cy="60" r="9" fill="none" stroke="#fff" stroke-width="3"/><circle cx="978" cy="74" r="9" fill="none" stroke="#fff" stroke-width="3"/>
</svg>
<div class="abs benefit" style="left:48px;top:1815px"><h3>100% Natural</h3><p>Lorem ipsum dolor sit amet, consectetur adipiscing elit, sed do eiusmod tempor incididunt ut labore et dolore magna aliqua.</p></div>
<div class="abs benefit" style="left:428px;top:1805px"><h3>Optimisers<br>Testosterone Levels</h3><p>Lorem ipsum dolor sit amet, consectetur adipiscing elit, sed do eiusmod tempor incididunt ut labore et dolore magna aliqua.</p></div>
<div class="abs benefit" style="left:815px;top:1805px"><h3>Optimisers<br>Sperm Production</h3><p>Lorem ipsum dolor sit amet, consectetur adipiscing elit, sed do eiusmod tempor incididunt ut labore et dolore magna aliqua.</p></div>

<!-- Why use -->
<h2 class="abs section-title center" style="left:0;top:2062px;width:1165px;line-height:56px">WHY USE<br><b>VELDER CREST</b></h2>
<div class="abs bottle" style="left:472px;top:2268px;width:240px;height:375px" role="img" aria-label="Supplement bottle with red and yellow capsules"></div>
<svg width="0" height="0" style="position:absolute"><defs><g id="tick"><circle cx="42" cy="48" r="38" fill="none" stroke="var(--blue)" stroke-width="6"/><path d="M20 46l20 24 44-60" fill="none" stroke="var(--blue)" stroke-width="10" stroke-linejoin="round"/></g></defs></svg>
<div class="abs why-item" style="left:94px;top:2298px;width:190px;text-align:right"><h4>LOREM IPSUM</h4><p>Lorem ipsum dolor sit amet, consectetur adipiscing elit, sed do eiusmod tempor incididunt</p></div>
<svg class="abs tick" style="left:300px;top:2282px"><use href="#tick"/></svg>
<div class="abs why-item" style="left:94px;top:2452px;width:190px;text-align:right"><h4>LOREM IPSUM</h4><p>Lorem ipsum dolor sit amet, consectetur adipiscing elit, sed do eiusmod tempor incididunt</p></div>
<svg class="abs tick" style="left:300px;top:2436px"><use href="#tick"/></svg>
<div class="abs why-item" style="left:94px;top:2612px;width:190px;text-align:right"><h4>LOREM IPSUM</h4><p>Lorem ipsum dolor sit amet, consectetur adipiscing elit, sed do eiusmod tempor incididunt</p></div>
<svg class="abs tick" style="left:300px;top:2596px"><use href="#tick"/></svg>
<svg class="abs tick" style="left:796px;top:2278px"><use href="#tick"/></svg>
<div class="abs why-item" style="left:900px;top:2293px;width:200px"><h4>LOREM IPSUM</h4><p>Lorem ipsum dolor sit amet, consectetur adipiscing elit, sed do eiusmod tempor incididunt</p></div>
<svg class="abs tick" style="left:792px;top:2442px"><use href="#tick"/></svg>
<div class="abs why-item" style="left:894px;top:2458px;width:200px"><h4>LOREM IPSUM</h4><p>Lorem ipsum dolor sit amet, consectetur adipiscing elit, sed do eiusmod tempor incididunt</p></div>
<svg class="abs tick" style="left:792px;top:2596px"><use href="#tick"/></svg>
<div class="abs why-item" style="left:894px;top:2622px;width:200px"><h4>LOREM IPSUM</h4><p>Lorem ipsum dolor sit amet, consectetur adipiscing elit, sed do eiusmod tempor incididunt</p></div>
<div class="abs btn blue" style="left:524px;top:2720px;width:143px;height:38px;font-size:14px">Buy Now</div>

<!-- Revive -->
<div class="abs" style="left:4px;top:2838px;width:604px;height:387px;background:var(--blue)"></div>
<div class="abs" style="left:608px;top:2838px;width:544px;height:387px;background:linear-gradient(90deg,#b46a3a,#c9b9ad 45%,#e9e8ec)" role="img" aria-label="Smiling couple, man holding a supplement bottle"></div>
<h2 class="abs section-title" style="left:70px;top:2910px;font-size:41px;line-height:52px">REVIVIE YOUR<br>VERTALITY</h2>
<p class="abs small" style="left:74px;top:3024px;width:300px;color:#fff">Lorem ipsum dolor sit amet, consectetur adipiscing elit, sed do eiusmod tempor incididunt ut labore et dolore magna aliqua.</p>
<div class="abs btn black" style="left:70px;top:3111px;width:143px;height:38px;font-size:14px">Order Now</div>

<!-- Testimonials -->
<div class="abs review" style="left:93px;top:3378px"><div class="stars">★★★★★</div><p>Ruis aute irure dolor in reprehender voluptate velit esse cillum dolore fugiat pariatur sint occaecat cupidata non proie sunt in culpa aui officede</p></div>
<div class="abs person" style="left:147px;top:3555px"><div class="avatar"></div><div><b>Mara Quill</b><small>Company Worker</small></div></div>
<div class="abs quote" style="left:362px;top:3600px">“</div>
<div class="abs review" style="left:453px;top:3378px"><div class="stars">★★★★★</div><p>Duis aute irure dolor in reprehender voluptate velit esse cillum dolore fugiat nulla pariatur sint occaecat cupidata non proident, sunt in culpa aui office deserunt mollit anim laborum.</p></div>
<div class="abs person" style="left:505px;top:3578px"><div class="avatar"></div><div><b>Tobin Hale</b><small>Assitant Manager</small></div></div>
<div class="abs quote" style="left:722px;top:3623px">“</div>
<div class="abs review" style="left:813px;top:3378px"><div class="stars">★★★★★</div><p>Ruis aute irure dolor in reprehender voluptate velit esse cillum dolore fugiat pariatur sint occaecat cupidata non proie sunt in culpa aui officede</p></div>
<div class="abs person" style="left:867px;top:3555px"><div class="avatar"></div><div><b>Rufus Venn</b><small>Company Worker</small></div></div>
<div class="abs quote" style="left:1082px;top:3600px">“</div>
<svg class="abs" style="left:570px;top:3696px" width="66" height="20"><circle cx="10" cy="10" r="5" fill="#ddd"/><circle cx="34" cy="10" r="8" fill="var(--blue)"/><circle cx="56" cy="10" r="5" fill="#ddd"/></svg>

<!-- Footer -->
<footer class="abs footer">
  <div class="abs brand" style="left:80px;top:170px;color:#fff"><i></i>Velder Crest</div>
  <div class="abs" style="left:337px;top:98px"><h5>QUICK LINKS</h5><ul style="margin-top:18px"><li>HOME</li><li>ABOUT</li><li>FAQS</li><li>BUY NOW</li></ul></div>
  <div class="abs" style="left:642px;top:98px"><h5>CONTACT INFO</h5><ul style="margin-top:22px"><li>PHONE : (123) 456 7890</li><li>E-MAIL : info@website.com</li><li>LOCATION : United States</li></ul></div>
  <div class="abs" style="left:998px;top:92px"><h5>SIGNUP</h5>
    <div style="margin-top:14px;width:145px;height:28px;background:#fff;color:#999;font-size:9px;padding:8px 12px">Email Address</div>
    <div class="btn blue" style="margin-top:16px;width:145px;height:28px;font-size:11px">Signup Now</div>
  </div>
</footer>
<div class="abs copy"><span class="abs" style="left:75px;top:16px">Copyright © 2013. All Rights Reserved</span>
  <span class="abs social" style="left:1050px"></span><span class="abs social" style="left:1087px"></span><span class="abs social" style="left:1124px"></span>
</div>

</body>
</html>
```